Energy trading company (Voltrisa) needs a business card

We need a business card for a company based in Central America. Our main purpose is trading energy . We already have the logo but we need some good creativity to design a high impact business card. Colors blue, orange, green can be used or we would like to see good combinatios with our logo

Target Market(s)

Energy

Industry/Entity Type

Power Generation

Contact Information for Business Card

Logo , headquarters , name, background

Font styles to use
Serif
Sans Serif

Colors

Designer to choose colors to be used in the design.

Requirements
Must have
• it must have a fresh and clean view
Nice to have
• good backgrounds that combine with the logo
Should not have
• too much words

```html
<!DOCTYPE html>
<html lang="en">
<head>
<meta charset="UTF-8">
<title>Voltrisa Business Card</title>
<link rel="stylesheet" href="https://fonts.googleapis.com/css2?family=Open+Sans:wght@400;600;700&display=swap">
<style>
  :root {
    --backdrop: #1c1c1e;
    --backdrop-light: #2e2e30;
    --card: #0b0b0d;
    --orange: #f5821f;
    --white: #f4f4f4;
  }
  html, body {
    margin: 0;
    width: 1200px;
    height: 900px;
    overflow: hidden;
  }
  body {
    background: radial-gradient(ellipse at 70% 10%, var(--backdrop-light), var(--backdrop) 70%);
    font-family: "Open Sans", Arial, sans-serif;
    position: relative;
  }
  .card {
    position: absolute;
    left: 280px;
    width: 640px;
    height: 366px;
    background: var(--card);
    box-shadow: 0 10px 28px rgba(0,0,0,0.55);
    overflow: hidden;
  }
  .card--front { top: 64px; }
  .card--back { top: 470px; }
  .card__band {
    position: absolute;
    left: 0; right: 0; bottom: 0;
    height: 14px;
    background: var(--orange);
  }
  .wordmark {
    position: absolute;
    left: 0; right: 0;
    top: 138px;
    text-align: center;
    color: var(--orange);
    font-weight: 600;
    font-size: 60px;
    letter-spacing: 4px;
    line-height: 1;
  }
  .identity {
    position: absolute;
    right: 362px;
    top: 142px;
    text-align: right;
  }
  .identity__name {
    color: var(--orange);
    font-weight: 700;
    font-size: 24px;
    letter-spacing: 1px;
    margin: 0;
    line-height: 1.2;
  }
  .identity__role {
    color: var(--white);
    font-weight: 600;
    font-size: 19px;
    letter-spacing: 1px;
    margin: 6px 0 0;
  }
  .divider {
    position: absolute;
    left: 298px;
    top: 148px;
    width: 2px;
    height: 70px;
    background: var(--orange);
  }
  .contacts {
    position: absolute;
    left: 318px;
    top: 144px;
    margin: 0;
    padding: 0;
    list-style: none;
  }
  .contacts__item {
    display: flex;
    align-items: center;
    gap: 10px;
    color: var(--white);
    font-size: 16px;
    line-height: 26px;
    letter-spacing: 0.5px;
  }
  .contacts__icon {
    width: 13px;
    height: 13px;
    flex: none;
  }
</style>
</head>
<body>
  <section class="card card--front">
    <div class="wordmark">VOLTRISA</div>
    <div class="card__band"></div>
  </section>

  <section class="card card--back">
    <div class="identity">
      <p class="identity__name">MAREN CASTELL</p>
      <p class="identity__role">Owner</p>
    </div>
    <div class="divider"></div>
    <ul class="contacts">
      <li class="contacts__item">
        <svg class="contacts__icon" viewBox="0 0 24 24" aria-hidden="true">
          <path fill="#f5821f" d="M6.6 10.8a15 15 0 0 0 6.6 6.6l2.2-2.2c.3-.3.7-.4 1-.2 1.1.4 2.3.6 3.6.6.6 0 1 .4 1 1V20c0 .6-.4 1-1 1A17 17 0 0 1 3 4c0-.6.4-1 1-1h3.5c.6 0 1 .4 1 1 0 1.3.2 2.5.6 3.6.1.3 0 .7-.2 1z"/>
        </svg>
        (555) 018-2746
      </li>
      <li class="contacts__item">
        <svg class="contacts__icon" viewBox="0 0 24 24" aria-hidden="true">
          <rect x="2" y="5" width="20" height="14" fill="none" stroke="#f5821f" stroke-width="2.5"/>
          <path d="M2 5l10 8 10-8" fill="none" stroke="#f5821f" stroke-width="2.5"/>
        </svg>
        info@voltrisa.com
      </li>
      <li class="contacts__item">
        <svg class="contacts__icon" viewBox="0 0 24 24" aria-hidden="true">
          <circle cx="12" cy="12" r="10" fill="none" stroke="#f5821f" stroke-width="2.5"/>
          <path d="M2 12h20M12 2c3 3 3 17 0 20M12 2c-3 3-3 17 0 20" fill="none" stroke="#f5821f" stroke-width="2"/>
        </svg>
        www.voltrisa.com
      </li>
    </ul>
    <div class="card__band"></div>
  </section>
</body>
</html>
```